Design a calming beauty medical salon & spa website based in Hong Kong

We need help building an informational website for a beauty salon in Hong Kong. The local salon provides facials, massages, body and other slimming treatments in a relaxing environment. We offer some non-invasive medical treatments, such as botox. Having built the business on word of mouth, it is now time for us to launch a website to help market the business better. Website requirements:

-Must be responsive
-Use vibrant but clean colours. not too many, 1-2 colours
-Must be bilingual (switch between Chinese traditional and English)
-Our current website is host on a server, not using any particular platforms like wordpress

Pages:
1/ Homepage
2/ About us (incorporate gallery of salon photos and history of company)
3/ Promotions and latest deals (and leads them to sign up for more info, maybe pop-up small window when you click on a promotion)
4/ Treatment menus
4.1/Body treatments
4.2/ Face treatments
4.3/ Slimming treatments
5/ Showcasing products sold (no e-commerce functionality, just showing off products)
6/ Contact us (tel, address, map, opening hrs)

Footer - must haves include contact us info, privacy policy, terms & conditions, copyright blurb, join our company/employment page (with a form)

For information (comparable websites we like):
http://vostaria.com/
http://quimbel.com.hk/tc/aboutquimbel/background.php#centerenvi
Attaching a very first draft concept for this website
Attaching pictures of the beauty salon
Attaching logo

Target Market(s)

Hong Kong based, Chinese, females, 30-50+ age. 90% female clients.

Industry/Entity Type

Beauty Salon

Number of Pages Required

5+ page

Font styles to use
Sans Serif

Colors
f9d9e8
fbd3d4
fee3d5
fbe7d2
fee18a
fbf289
ffffff

Requirements
Must have
• interactive elements on website, such as scrolling banner photo headers
• incorporate photos of website salon
• connect to facebook page

```html
<!DOCTYPE html>
<html lang="en">
<head>
<meta charset="utf-8">
<title>Serene Beauty – Home</title>
<link rel="stylesheet" href="https://fonts.googleapis.com/css2?family=Open+Sans:wght@400;600;700&display=swap">
<style>
:root{
  --purple:#6b1d7c;
  --ink:#1e1e1e;
  --muted:#555;
  --pink-line:#f6d4d6;
  --hero-pink:#f8d4d3;
  --pill:#fee18a;
  --yellow-top:#fbef8f;
  --yellow-bottom:#fde28a;
  --contact-a:#f6dcd2;
  --contact-b:#f1cfc6;
  --fb-blue:#1f4e9c;
  --white:#ffffff;
}
*{box-sizing:border-box;margin:0;padding:0}
html,body{width:1200px;height:2532px;overflow:hidden}
body{position:relative;font-family:"Open Sans",Arial,sans-serif;color:var(--ink);background:var(--white)}
.abs{position:absolute}

/* header */
.top-line{left:0;top:0;width:1200px;height:5px;background:var(--pink-line)}
.site-header{left:0;top:5px;width:1200px;height:122px;background:var(--white)}
.brand{display:flex;align-items:center;gap:10px;color:var(--purple);font-weight:700;white-space:nowrap}
.brand-dot{border-radius:50%;background:var(--purple);flex:none}
.header-brand{left:98px;top:45px;font-size:24px}
.header-brand .brand-dot{width:30px;height:30px}
.round-social{width:34px;height:34px;border-radius:50%;background:var(--fb-blue)}
.top-social{left:618px;top:14px}
.top-item{top:14px;height:34px;display:flex;align-items:center;gap:8px;font-size:15px;color:#666;white-space:nowrap}
.flag{top:21px;width:30px;height:20px}
.flag-en{left:1030px;background:#2d3f8c}
.flag-zh{left:1071px;background:#e2322b}
.nav-link{top:64px;height:36px;line-height:36px;font-size:14px;color:var(--ink);white-space:nowrap}
.nav-link.active{background:var(--pill);border-radius:18px;width:81px;text-align:center}

/* hero */
.hero{left:0;top:127px;width:1200px;height:498px;background:var(--hero-pink)}
.hero-photo{left:0;top:0;width:1200px;height:498px;
  background:
    radial-gradient(ellipse 180px 260px at 250px 170px,#f1c2ad 0%,rgba(241,194,173,0) 100%),
    radial-gradient(ellipse 150px 220px at 170px 120px,#4a3431 0%,rgba(74,52,49,.6) 45%,rgba(74,52,49,0) 100%),
    radial-gradient(ellipse 260px 200px at 360px 430px,#f3c7b4 0%,rgba(243,199,180,0) 100%),
    radial-gradient(ellipse 420px 420px at 300px 240px,#f5cabd 0%,rgba(245,202,189,0) 100%),
    linear-gradient(90deg,#f4cfc6 0%,#f8d6d3 55%,#f9d4d4 100%)}
.hero-brand{left:633px;top:288px;font-size:42px}
.hero-brand .brand-dot{width:52px;height:52px}
.hero-tag{left:744px;top:361px;font-size:20px;font-weight:700;color:var(--ink);white-space:nowrap}
.hero-dots{left:547px;top:579px;display:flex;gap:18px}
.hero-dots span{width:12px;height:12px;border-radius:50%;background:#222}
.hero-dots span.on{background:var(--white)}

/* services */
.services-title{left:0;top:676px;width:1200px;text-align:center;font-size:28px;font-weight:700}
.services-text{left:0;top:733px;width:1200px;text-align:center;font-size:13.5px;line-height:31px;color:var(--ink)}
.service{width:242px;height:274px;top:872px}
.service svg{position:absolute;left:0;top:0}
.service-label{position:absolute;left:0;top:0;width:242px;height:274px;display:flex;align-items:center;justify-content:center;text-align:center;font-size:27px;font-weight:700;line-height:31px;color:var(--white)}
.service-face .service-label{color:#3b2a12}
.svc-1{left:169px}.svc-2{left:479px}.svc-3{left:790px}

/* contact */
.contact{left:0;top:1217px;width:1200px;height:676px;
  background:
    radial-gradient(ellipse 200px 170px at 1110px 90px,#f49a8a 0%,rgba(244,154,138,0) 100%),
    radial-gradient(ellipse 160px 120px at 850px 40px,#f7b7a8 0%,rgba(247,183,168,0) 100%),
    radial-gradient(ellipse 150px 260px at 30px 340px,rgba(120,150,110,.55) 0%,rgba(120,150,110,0) 100%),
    radial-gradient(ellipse 130px 120px at 150px 640px,rgba(214,180,110,.6) 0%,rgba(214,180,110,0) 100%),
    radial-gradient(ellipse 120px 160px at 1150px 430px,rgba(214,180,110,.55) 0%,rgba(214,180,110,0) 100%),
    linear-gradient(135deg,var(--contact-a),var(--contact-b) 60%,#f4d6cb)}
.contact-title{left:0;top:1272px;width:1200px;text-align:center;font-size:29px;font-weight:700}
.info-head{display:flex;align-items:center;gap:12px;font-size:21px;font-weight:700}
.info-head svg{flex:none}
.info-line{font-size:14.5px;color:var(--ink)}
.map{left:536px;top:1386px;width:566px;height:397px;
  background:
    linear-gradient(160deg,rgba(255,255,255,.55),rgba(255,255,255,0) 40%),
    radial-gradient(ellipse 120px 80px at 290px 120px,#efe1c4 0%,rgba(239,225,196,0) 100%),
    radial-gradient(ellipse 200px 140px at 120px 300px,#e7dcc8 0%,rgba(231,220,200,0) 100%),
    linear-gradient(160deg,#f0e6d6,#e5ddd1 50%,#ece3d5)}

/* join */
.join{left:0;top:1893px;width:1200px;height:419px;background:linear-gradient(var(--yellow-top),var(--yellow-bottom))}
.join-title{left:0;top:1923px;width:1200px;text-align:center;font-size:29px;font-weight:700}
.field{background:var(--white);font-size:14px;color:var(--ink);padding:0 20px;display:flex;align-items:center}
.field-message{align-items:flex-start;padding-top:14px}
.submit{left:539px;top:2237px;width:122px;height:36px;border-radius:18px;background:var(--purple);color:var(--white);font-size:14px;font-weight:700;display:flex;align-items:center;justify-content:center}

/* footer */
.footer-brand{left:0;top:2343px;width:1200px;justify-content:center;font-size:21px;gap:8px}
.footer-brand .brand-dot{width:26px;height:26px}
.footer-social{left:583px;top:2401px}
.footer-links{left:0;top:2454px;width:1200px;text-align:center;font-size:15px}
.footer-links span.sep{margin:0 16px}
.copyright{left:0;top:2488px;width:1200px;text-align:center;font-size:13.5px}
</style>
</head>
<body>

<div class="abs top-line"></div>
<header class="abs site-header"></header>
<div class="abs brand header-brand"><span class="brand-dot"></span>Serene Beauty</div>

<span class="abs round-social top-social" role="img" aria-label="Social page link"></span>
<span class="abs top-item" style="left:664px">
  <svg width="14" height="18" viewBox="0 0 14 18"><rect x="2" y="1" width="10" height="16" rx="2" fill="none" stroke="#555" stroke-width="1.8"/><circle cx="7" cy="14" r="1" fill="#555"/></svg>
  Tel: 2388 4150
</span>
<span class="abs top-item" style="left:817px">
  <svg width="18" height="18" viewBox="0 0 18 18"><circle cx="9" cy="9" r="7.5" fill="none" stroke="#555" stroke-width="1.6"/><path d="M6 6.5c0 3 2.5 5.5 5.5 5.5" fill="none" stroke="#555" stroke-width="1.6" stroke-linecap="round"/></svg>
  Mobile: 6152 0937
</span>
<span class="abs flag flag-en" role="img" aria-label="English"></span>
<span class="abs flag flag-zh" role="img" aria-label="Traditional Chinese"></span>

<nav>
  <a class="abs nav-link active" style="left:397px">Home</a>
  <a class="abs nav-link" style="left:488px">About Us</a>
  <a class="abs nav-link" style="left:579px">Promotions &amp; Latest deals</a>
  <a class="abs nav-link" style="left:778px">Treatment</a>
  <a class="abs nav-link" style="left:878px">Products Showcase</a>
  <a class="abs nav-link" style="left:1033px">Contact us</a>
</nav>

<section class="abs hero">
  <div class="abs hero-photo" role="img" aria-label="Banner photo of a smiling woman touching her glowing skin"></div>
</section>
<div class="abs brand hero-brand"><span class="brand-dot"></span>Serene Beauty</div>
<div class="abs hero-tag">Excellent medical beauty</div>
<div class="abs hero-dots"><span></span><span></span><span class="on"></span><span></span></div>

<h2 class="abs services-title">A full range of beauty services</h2>
<p class="abs services-text">
  To take care of all aspects of the skin different needs, providing facial and body care,<br>
  Customers can enjoy a more efficient and beautiful skin treatment in a relaxed and comfortable environment.<br>
  Together with the noble Swiss brand Serene Beauty organic material series for home care,<br>
  In order to push the quality of skin to the pinnacle.
</p>

<svg width="0" height="0" style="position:absolute">
  <defs>
    <linearGradient id="gFace" x1="0" y1="0" x2="1" y2="1"><stop offset="0" stop-color="#f8e08e"/><stop offset="1" stop-color="#f1c862"/></linearGradient>
    <linearGradient id="gBody" x1="0" y1="0" x2="1" y2="1"><stop offset="0" stop-color="#8a7a74"/><stop offset=".5" stop-color="#3e3330"/><stop offset="1" stop-color="#d8c6bc"/></linearGradient>
    <linearGradient id="gSlim" x1="0" y1="0" x2="1" y2="1"><stop offset="0" stop-color="#c9a792"/><stop offset=".5" stop-color="#5a4036"/><stop offset="1" stop-color="#e4cfc2"/></linearGradient>
  </defs>
</svg>

<div class="abs service service-face svc-1">
  <svg width="242" height="274" viewBox="0 0 242 274" role="img" aria-label="Photo of yellow facial cream"><polygon points="121,14 230,75 230,199 121,260 12,199 12,75" fill="url(#gFace)" stroke="url(#gFace)" stroke-width="24" stroke-linejoin="round"/></svg>
  <div class="service-label">Face<br>Treatments</div>
</div>
<div class="abs service svc-2">
  <svg width="242" height="274" viewBox="0 0 242 274" role="img" aria-label="Photo of a hot stone back massage"><polygon points="121,14 230,75 230,199 121,260 12,199 12,75" fill="url(#gBody)" stroke="url(#gBody)" stroke-width="24" stroke-linejoin="round"/></svg>
  <div class="service-label">Body<br>Treatments</div>
</div>
<div class="abs service svc-3">
  <svg width="242" height="274" viewBox="0 0 242 274" role="img" aria-label="Photo of a slimming body treatment"><polygon points="121,14 230,75 230,199 121,260 12,199 12,75" fill="url(#gSlim)" stroke="url(#gSlim)" stroke-width="24" stroke-linejoin="round"/></svg>
  <div class="service-label">Slimming<br>Treatments</div>
</div>

<section class="abs contact" role="img" aria-label="Background photo of flowers, leaves and oil bottles"></section>
<h2 class="abs contact-title">Contact Us</h2>

<div class="abs info-head" style="left:112px;top:1366px">
  <svg width="18" height="18" viewBox="0 0 18 18"><circle cx="9" cy="9" r="7.5" fill="none" stroke="#1e1e1e" stroke-width="2"/><path d="M9 4.5V9l3 2" fill="none" stroke="#1e1e1e" stroke-width="2" stroke-linecap="round"/></svg>
  Opening Hours
</div>
<div class="abs info-line" style="left:145px;top:1410px">Monday to Friday: 10:30 am to 9:30 pm</div>
<div class="abs info-line" style="left:145px;top:1441px">Saturday and holidays: 10:30 am to 7:30 pm</div>

<div class="abs info-head" style="left:112px;top:1487px">
  <svg width="18" height="18" viewBox="0 0 24 24"><path d="M6.6 10.8a15.1 15.1 0 0 0 6.6 6.6l2.2-2.2a1 1 0 0 1 1-.25 11.4 11.4 0 0 0 3.6.57 1 1 0 0 1 1 1V20a1 1 0 0 1-1 1A17 17 0 0 1 3 4a1 1 0 0 1 1-1h3.5a1 1 0 0 1 1 1c0 1.25.2 2.45.57 3.57a1 1 0 0 1-.25 1z" fill="#1e1e1e"/></svg>
  Inquiry Hotline
</div>
<div class="abs info-line" style="left:145px;top:1532px">23884150</div>
<div class="abs info-line" style="left:145px;top:1562px">61520937</div>

<div class="abs info-head" style="left:112px;top:1609px">
  <svg width="16" height="20" viewBox="0 0 16 20"><path d="M8 0a8 8 0 0 1 8 8c0 5.5-8 12-8 12S0 13.5 0 8a8 8 0 0 1 8-8z" fill="#1e1e1e"/><circle cx="8" cy="8" r="3" fill="#f4d6cb"/></svg>
  <span style="margin-left:8px">Address</span>
</div>
<div class="abs info-line" style="left:145px;top:1654px">12th Floor, Jade Harbour Centre, 52-54 Lotus Road</div>
<div class="abs info-line" style="left:145px;top:1684px">Tsim Sha Tsui, Kowloon</div>

<div class="abs info-head" style="left:112px;top:1731px">
  <svg width="20" height="15" viewBox="0 0 20 15"><rect x="1" y="1" width="18" height="13" fill="none" stroke="#1e1e1e" stroke-width="1.8"/><path d="M1 1l9 7 9-7" fill="none" stroke="#1e1e1e" stroke-width="1.8"/></svg>
  <span style="margin-left:8px">hello@serenebeauty.hk</span>
</div>

<div class="abs map" role="img" aria-label="Street map showing the salon location in Tsim Sha Tsui"></div>

<section class="abs join"></section>
<h2 class="abs join-title">Join Our Company</h2>
<div class="abs field" style="left:245px;top:1996px;width:341px;height:44px">First Name</div>
<div class="abs field" style="left:613px;top:1996px;width:344px;height:44px">Last Name</div>
<div class="abs field" style="left:245px;top:2057px;width:712px;height:44px">Email</div>
<div class="abs field field-message" style="left:245px;top:2119px;width:712px;height:95px">Message</div>
<div class="abs submit">Submit</div>

<div class="abs brand footer-brand"><span class="brand-dot"></span>Serene Beauty</div>
<span class="abs round-social footer-social" role="img" aria-label="Social page link"></span>
<div class="abs footer-links">Terms and conditions<span class="sep">|</span>Privacy Policy<span class="sep">|</span>join us</div>
<div class="abs copyright">Copyright © 2018 Serene Beauty HK Ltd. All rights reserved.</div>

</body>
</html>
```